Zorpax.com (Dedicated servers Provider)

We provide dedicated servers for clients around the world. We have created a layout for you. You need to create exactly the design based on these sketches. All text, you can take from our sketches (later we will replace them).

Target Market(s)

Web site owners and web developers

Requirements
Should not have
• The design should not use old-style fonts.

```html
<!DOCTYPE html>
<html lang="en">
<head>
<meta charset="utf-8">
<title>Zorpax Servers – Dedicated Servers Provider</title>
<link href="https://fonts.googleapis.com/css2?family=Open+Sans:ital,wght@0,400;0,600;0,700;0,800;1,400;1,600&display=swap" rel="stylesheet">
<style>
:root{
  --green:#7dbb2a;
  --green-dark:#5f9a17;
  --green-light:#a6d85a;
  --ink:#222;
  --grey:#666;
  --light:#f2f2f2;
  --line:#d9d9d9;
  --dark:#1d1d1d;
  --white:#fff;
  --red:#d8221b;
}
*{box-sizing:border-box;margin:0;padding:0}
html,body{width:1200px;height:2697px;overflow:hidden}
body{font-family:"Open Sans",Arial,sans-serif;color:var(--ink);background:var(--white);position:relative}
.wrap{width:1160px;margin:0 auto;position:relative}

/* header */
.site-header{height:124px;position:relative}
.brand{position:absolute;left:20px;top:22px;display:flex;align-items:center;gap:12px}
.brand-mark{width:40px;height:40px;background:var(--green)}
.brand-name{font-size:52px;font-weight:800;letter-spacing:-1px;color:#333;line-height:1}
.contact-line{position:absolute;right:20px;top:8px;display:flex;align-items:center;gap:10px;font-size:19px;font-weight:600}
.contact-line .q{width:34px;height:34px;border-radius:50%;background:#111;color:#fff;display:flex;align-items:center;justify-content:center;font-weight:800;font-size:22px}
.contact-line .num{color:var(--green);font-size:30px;font-weight:700}
.account-links{position:absolute;right:20px;top:70px;display:flex;gap:14px}
.account-links a{background:linear-gradient(#3a3a3a,#161616);color:#fff;font-size:13px;font-weight:600;padding:6px 16px;border-radius:8px;text-decoration:none;text-transform:uppercase}

.main-nav{height:51px;background:linear-gradient(#4a4a4a,#2a2a2a);display:flex;align-items:stretch;padding-left:18px;padding-right:22px}
.main-nav .home{width:72px;background:var(--green);display:flex;align-items:center;justify-content:center}
.main-nav ul{display:flex;list-style:none;flex:1}
.main-nav li{width:166px;display:flex;align-items:center;justify-content:center;color:#fff;font-size:15px;border-right:1px solid #555}
.main-nav .order{width:208px;background:linear-gradient(var(--green-light),var(--green));color:#fff;font-weight:700;font-size:21px;display:flex;align-items:center;justify-content:center}

.notice-bar{height:32px;background:linear-gradient(#b6e070,#8ccb3a);display:flex;align-items:center;padding:0 22px 0 112px;font-size:14px;color:#222}
.notice-bar .msg{flex:1}
.notice-bar .msg b{font-weight:600;color:#fff}
.follow{display:flex;align-items:center;gap:6px;font-weight:600}
.follow span.soc{width:24px;height:24px;border-radius:4px}

/* hero */
.hero{height:418px;background:radial-gradient(ellipse at 40% 40%,#3b3b3b,#151515 70%);position:relative;overflow:hidden}
.hero-servers{position:absolute;left:18px;top:22px;width:390px;height:385px;background:linear-gradient(160deg,#454545,#151515 70%);opacity:.9}
.hero-copy{position:absolute;left:258px;top:42px;color:#fff}
.hero-copy h1{font-size:43px;font-weight:700;line-height:1}
.hero-copy .from{display:block;text-align:right;font-size:17px;font-style:italic;margin:8px 0 18px;font-weight:600}
.hero-copy ul{list-style:none;font-size:17px;line-height:33px}
.hero-copy li::before{content:"»";margin-right:14px;color:#bbb}
.btn-green{display:inline-block;background:linear-gradient(var(--green-light),var(--green-dark));color:#fff;font-weight:600;text-transform:uppercase;border-radius:3px}
.hero-copy .btn-green{margin:18px 0 0 24px;font-size:17px;padding:8px 22px}
.hero-photo{position:absolute;left:700px;top:0;width:500px;height:418px;background:linear-gradient(90deg,#1e1e1e,#3a3a3a 35%,#9a9a9a 70%,#d0d0d0)}
.hero-quote{position:absolute;left:722px;top:62px;width:340px;color:#fff;font-style:italic;font-size:25px;line-height:36px}
.hero-quote::before{content:"\201C";position:absolute;left:-2px;top:-14px;font-size:64px;color:#777}
.hero-quote p{padding-left:30px}
.hero-quote cite{display:block;text-align:right;font-size:16px;color:#ccc;margin-top:4px;padding-right:30px}

.hiring-bar{height:90px;background:linear-gradient(#f4f4f4,#dcdcdc);position:relative}
.hiring-icon{position:absolute;left:28px;top:18px;width:44px;height:56px;background:linear-gradient(#444,#111);border-radius:22px 22px 4px 4px}
.hiring-text{position:absolute;left:98px;top:18px}
.hiring-text h3{font-size:20px;font-weight:700;color:#222}
.hiring-text .btn-green{font-size:12px;padding:3px 8px;margin-top:4px}
.sales-line{position:absolute;right:22px;top:26px;font-size:30px;font-weight:600;color:#333}
.sales-line b{font-weight:700;color:#222}

/* plans */
.plan-tabs{margin-top:45px;display:flex;height:49px;background:#2c2c2c}
.plan-tabs li{list-style:none;width:274px;display:flex;align-items:center;justify-content:center;color:#fff;font-size:16px;font-weight:600}
.plan-tabs li.active{background:linear-gradient(var(--green-light),var(--green))}
.plans{border:1px solid var(--line);border-top:0;height:337px;display:flex;padding:20px 0}
.plan{flex:1;padding:8px 20px 0 20px;border-right:1px solid var(--line);position:relative}
.plan:last-child{border-right:0}
.plan h2{font-size:25px;font-weight:600;text-align:center;color:#222}
.plan-visual{width:216px;height:72px;margin:18px auto 16px;background:linear-gradient(90deg,#4f8a2a 0 38%,#c9c9c9 38%,#9e9e9e);border:1px solid #999}
.plan-price{display:flex;align-items:flex-start;gap:10px;padding-left:6px}
.price{display:flex;align-items:flex-start;color:var(--red);font-weight:700}
.price .from{position:absolute;font-size:12px;color:#333;font-weight:400;margin-top:-18px}
.price .cur{font-size:30px;margin-top:8px}
.price .amt{font-size:52px;line-height:1}
.price .cents{font-size:25px;line-height:1.2;display:flex;flex-direction:column}
.price .cents small{font-size:11px;color:#333;font-weight:400}
.specs{font-size:12.5px;line-height:18px;color:#333}
.term{margin-top:6px;border:1px solid #aaa;border-radius:4px;font-size:11px;padding:1px 10px;width:186px}
.plan-foot{position:absolute;left:38px;right:44px;top:262px;display:flex;justify-content:space-between;align-items:center}
.plan-foot a{font-size:13px;color:#222;text-decoration:underline;font-weight:600}
.plan-foot .btn-green{font-size:13px;padding:3px 14px}

.features{border:1px solid var(--line);border-top:0;height:220px;position:relative;background:linear-gradient(#fff,#f4f4f4)}
.features-map{position:absolute;left:28px;top:24px;width:250px;height:140px;background:radial-gradient(ellipse,#8fd43a,#c4c4c4 75%);border-radius:40% 30% 35% 45%}
.features-caption{position:absolute;left:52px;top:180px;font-size:11px;font-weight:600;color:#333}
.features ul{position:absolute;left:380px;top:44px;list-style:none;display:grid;grid-template-columns:395px 360px;row-gap:26px}
.features li{display:flex;align-items:center;gap:16px;font-size:18px;color:#222;white-space:nowrap}
.tick{width:28px;height:28px;flex:none}

/* testimonial */
.testimonial{margin-top:60px;height:168px;position:relative}
.testimonial .arrow{position:absolute;top:66px}
.testimonial .prev{left:18px}
.testimonial .next{right:18px}
.testimonial-photo{position:absolute;left:82px;top:0;width:200px;height:158px;border:6px solid #fff;box-shadow:0 0 4px #aaa;background:linear-gradient(#e6e6e6,#9a9a9a)}
.testimonial blockquote{position:absolute;left:320px;top:20px;width:780px;font-size:20px;font-style:italic;color:#999;line-height:29px}
.testimonial blockquote::before{content:"\201C";position:absolute;left:-38px;top:-18px;font-size:64px;color:#ccc}
.testimonial blockquote::after{content:"\201D";font-size:50px;color:#ccc;position:absolute;right:-34px;bottom:-36px}
.testimonial .author{position:absolute;left:322px;top:125px;font-size:15px;color:#888;line-height:22px}

.partners{margin-top:45px;height:113px;background:linear-gradient(#e2e2e2,#f5f5f5);display:flex;align-items:center;justify-content:space-around;padding:0 40px}
.partners span{background:#b9b9b9;opacity:.8}

/* dark footer */
.dark{position:absolute;left:0;top:1760px;width:1200px;height:937px;background:repeating-linear-gradient(45deg,var(--dark) 0 3px,#1a1a1a 3px 6px);color:#fff}
.dark h2{font-size:22px;font-weight:600;color:#fff}
.dark h2 span{color:var(--green)}
.services{position:absolute;left:36px;top:44px;width:1130px}
.service-grid{margin-top:34px;display:grid;grid-template-columns:repeat(3,1fr);row-gap:36px}
.service{display:flex;gap:26px}
.service svg{flex:none}
.service h4{font-size:14px;font-weight:700}
.service p{font-size:12.5px;color:#888;line-height:16px;margin-top:2px}
.divider{position:absolute;left:0;width:1200px;height:1px;background:#333}
.stats{position:absolute;left:36px;top:370px;width:1130px}
.stat-row{display:grid;grid-template-columns:repeat(4,1fr);margin-top:28px}
.stat{display:flex;gap:16px}
.stat .ic{width:20px;height:20px;border-radius:50%;background:#fff;margin-top:14px;flex:none;position:relative}
.stat .ic::after{content:"";position:absolute;left:7px;top:5px;border-left:7px solid var(--dark);border-top:5px solid transparent;border-bottom:5px solid transparent}
.stat b{font-size:40px;font-weight:600;display:block;line-height:1.2}
.stat small{font-size:11px;color:#888;display:block;line-height:14px}
.footer-cols{position:absolute;left:36px;top:590px;width:1130px;display:flex}
.footer-cols h3{font-size:20px;font-weight:600;color:var(--green);margin-bottom:10px}
.col-about{width:470px;font-size:14px;line-height:22px}
.col-about a{display:block;margin-top:20px;color:var(--green);font-weight:600;font-size:14px;text-decoration:none}
.col-links{width:355px}
.col-links ul{list-style:none;display:grid;grid-template-columns:130px 130px;font-size:14px;line-height:22px}
.col-links p{font-size:14px;line-height:22px;margin-top:16px}
.col-info{width:310px;font-size:14px;line-height:22px}
.col-info .phone{font-size:35px;font-weight:700;margin:8px 0}
.col-info .social{display:flex;gap:8px}
.col-info .social span{width:36px;height:36px;border-radius:50%}
.bottom-strip{position:absolute;left:0;top:835px;width:1200px;height:102px;background:#111;display:flex;align-items:center;padding:0 28px}
.bottom-strip .logos{display:flex;gap:30px;flex:1;align-items:center}
.bottom-strip .logos span{background:#d6d6d6}
.award{display:flex;align-items:center;gap:14px;margin-right:26px;text-align:center}
.award b{font-size:15px;font-weight:800;display:block;line-height:17px}
.award em{font-style:normal;font-size:10px;color:var(--green)}
.award .seal{width:70px;height:54px;border-radius:50%;background:radial-gradient(#eee,#888)}
.sitemap{border:1px solid #444;background:#222;font-size:13px;font-weight:600;padding:6px 14px}
</style>
</head>
<body>

<header class="site-header">
  <div class="brand"><span class="brand-mark"></span><span class="brand-name">zorpax</span></div>
  <div class="contact-line"><span class="q">?</span>Questions? Call Now! <span class="num">0.800.555.HOST</span></div>
  <nav class="account-links"><a href="#">User Registration</a><a href="#">Customer Login</a><a href="#">Live Chat Online</a></nav>
</header>

<nav class="main-nav">
  <div class="home"><svg width="30" height="26" viewBox="0 0 30 26"><path d="M15 2 2 13h4v11h7v-7h4v7h7V13h4z" fill="#fff"/></svg></div>
  <ul><li>Domains</li><li>Web Hosting</li><li>Latest News</li><li>My Account</li><li>Contact Us</li></ul>
  <div class="order">ORDER NOW!</div>
</nav>

<div class="notice-bar">
  <p class="msg">Got an important announcement or a special offer? Tell your customer about it! <b>Read More</b></p>
  <div class="follow">Follow Us <span class="soc" style="background:#3b5a9a"></span><span class="soc" style="background:#3aa4dd"></span><span class="soc" style="background:#f07d1e"></span></div>
</div>

<section class="hero">
  <div class="hero-photo" role="img" aria-label="Smiling businessman in a grey suit"></div>
  <div class="hero-servers" role="img" aria-label="Three black rack server towers"></div>
  <div class="hero-copy">
    <h1>DEDICATED SERVERS</h1>
    <span class="from">FROM ZORPAX</span>
    <ul>
      <li>Self-owned data centre</li>
      <li>24 x 7 x 365 on-site support</li>
      <li>100% uptime guarantee</li>
      <li>Industry leading control panel</li>
      <li>Custom servers; 24 hour setup</li>
    </ul>
    <span class="btn-green">Find out more</span>
  </div>
  <blockquote class="hero-quote"><p>Glad I managed to choose one of the few companies with good customer service</p><cite>trailpeak.co.uk</cite></blockquote>
</section>

<section class="hiring-bar">
  <div class="hiring-icon" role="img" aria-label="Person icon"></div>
  <div class="hiring-text"><h3>WE ARE HIRING</h3><span class="btn-green">Apply online now</span></div>
  <p class="sales-line">CALL SALES TODAY <b>01632 960 418</b></p>
</section>

<main class="wrap">
  <ul class="plan-tabs"><li class="active">Dedicated Servers</li><li>Web Hosting</li><li>Virtual Private Server</li></ul>
  <div class="plans">
    <article class="plan">
      <h2>Quantum 4 2.4 GHz</h2>
      <div class="plan-visual" role="img" aria-label="Processor and rack server unit"></div>
      <div class="plan-price">
        <div class="price"><span class="from">Plans starting at</span><span class="cur">$</span><span class="amt">39</span><span class="cents">00<small>per mo.</small></span></div>
        <div class="specs">80GB SATA HD<br>1GB RAM<br>1TB Bandwidth<div class="term">1 year – 39.00/mo &nbsp;▾</div></div>
      </div>
      <div class="plan-foot"><a href="#">All Dedicated Servers</a><span class="btn-green">Order</span></div>
    </article>
    <article class="plan">
      <h2>Vertex X7 2.66-2.93 GHz</h2>
      <div class="plan-visual" role="img" aria-label="Processor and rack server unit"></div>
      <div class="plan-price">
        <div class="price"><span class="from">Plans starting at</span><span class="cur">$</span><span class="amt">219</span><span class="cents">00<small>per mo.</small></span></div>
        <div class="specs">500GB SATA HD<br>6GB RAM<br>8TB Bandwidth<div class="term">1 year – 39.00/mo &nbsp;▾</div></div>
      </div>
      <div class="plan-foot"><a href="#">All Dedicated Servers</a><span class="btn-green">Order</span></div>
    </article>
    <article class="plan">
      <h2>Dual Helix H5-2600</h2>
      <div class="plan-visual" role="img" aria-label="Processor and rack server unit"></div>
      <div class="plan-price">
        <div class="price"><span class="from">Plans starting at</span><span class="cur">$</span><span class="amt">395</span><span class="cents">00<small>per mo.</small></span></div>
        <div class="specs">1000GB SATA HD<br>16GB RAM<br>10TB Bandwidth<div class="term">1 year – 39.00/mo &nbsp;▾</div></div>
      </div>
      <div class="plan-foot"><a href="#">All Dedicated Servers</a><span class="btn-green">Order</span></div>
    </article>
  </div>

  <section class="features">
    <div class="features-map" role="img" aria-label="Map of the United States with green network links"></div>
    <p class="features-caption">Now Offering Panelix Control Panel 11</p>
    <ul>
      <li><svg class="tick" viewBox="0 0 28 28"><circle cx="14" cy="14" r="14" fill="#7dbb2a"/><path d="M8 14l4 4 8-8" stroke="#fff" stroke-width="3" fill="none"/></svg>100% Network Uptime SLA</li>
      <li><svg class="tick" viewBox="0 0 28 28"><circle cx="14" cy="14" r="14" fill="#7dbb2a"/><path d="M8 14l4 4 8-8" stroke="#fff" stroke-width="3" fill="none"/></svg>3 SSAE-16 Certified Data Centers</li>
      <li><svg class="tick" viewBox="0 0 28 28"><circle cx="14" cy="14" r="14" fill="#7dbb2a"/><path d="M8 14l4 4 8-8" stroke="#fff" stroke-width="3" fill="none"/></svg>ISO 9001:2008 Certified</li>
      <li><svg class="tick" viewBox="0 0 28 28"><circle cx="14" cy="14" r="14" fill="#7dbb2a"/><path d="M8 14l4 4 8-8" stroke="#fff" stroke-width="3" fill="none"/></svg>Coast-to-Coast IP Backbone</li>
      <li><svg class="tick" viewBox="0 0 28 28"><circle cx="14" cy="14" r="14" fill="#7dbb2a"/><path d="M8 14l4 4 8-8" stroke="#fff" stroke-width="3" fill="none"/></svg>24/7 ITIL Technical Support</li>
      <li><svg class="tick" viewBox="0 0 28 28"><circle cx="14" cy="14" r="14" fill="#7dbb2a"/><path d="M8 14l4 4 8-8" stroke="#fff" stroke-width="3" fill="none"/></svg>Award Winning Since 1996</li>
    </ul>
  </section>

  <section class="testimonial">
    <svg class="arrow prev" width="18" height="44" viewBox="0 0 18 44"><path d="M16 2 3 22l13 20" stroke="#555" stroke-width="3" fill="none"/></svg>
    <div class="testimonial-photo" role="img" aria-label="Portrait of a smiling man in a suit"></div>
    <blockquote>Lorem Ipsum is simply dummy text of the printing and typesetting industry. Lorem Ipsum has been the industry's standard dummy text ever since the 1500s, Lorem Ipsum is simply dummy text of the printing and typesetting industry.</blockquote>
    <p class="author">Daniel Harrow | C.E.O.<br>harrowstudio.com</p>
    <svg class="arrow next" width="18" height="44" viewBox="0 0 18 44"><path d="M2 2l13 20L2 42" stroke="#555" stroke-width="3" fill="none"/></svg>
  </section>
</main>

<section class="partners" aria-label="Partners">
  <span style="width:56px;height:36px;border-radius:50%"></span>
  <span style="width:34px;height:44px"></span>
  <span style="width:74px;height:24px"></span>
  <span style="width:96px;height:36px"></span>
  <span style="width:76px;height:42px"></span>
  <span style="width:56px;height:56px;border-radius:50%"></span>
  <span style="width:72px;height:38px;border-radius:50%"></span>
  <span style="width:76px;height:22px"></span>
  <span style="width:62px;height:32px"></span>
  <span style="width:74px;height:28px"></span>
</section>

<footer class="dark">
  <section class="services">
    <h2><span>Zorpax Servers -</span> Dedicated servers Provider</h2>
    <div class="service-grid">
      <div class="service"><svg width="50" height="44" viewBox="0 0 50 44"><rect x="2" y="4" width="46" height="14" rx="3" fill="#fff"/><rect x="2" y="24" width="46" height="14" rx="3" fill="#fff"/><circle cx="40" cy="11" r="2" fill="#222"/><circle cx="40" cy="31" r="2" fill="#222"/></svg><div><h4>Lorem Ipsum is simply dummy text</h4><p>Lorem Ipsum is simply dummy text of the<br>printing and typesetting industry.</p></div></div>
      <div class="service"><svg width="50" height="50" viewBox="0 0 50 50"><circle cx="25" cy="25" r="21" stroke="#fff" stroke-width="3" fill="none"/><ellipse cx="25" cy="25" rx="9" ry="21" stroke="#fff" stroke-width="3" fill="none"/><path d="M4 25h42M8 14h34M8 36h34" stroke="#fff" stroke-width="3"/></svg><div><h4>Lorem Ipsum is simply dummy text</h4><p>Lorem Ipsum is simply dummy text of the<br>printing and typesetting industry.</p></div></div>
      <div class="service"><svg width="50" height="50" viewBox="0 0 50 50"><path d="M15 12a14 14 0 0 0 0 20M35 12a14 14 0 0 1 0 20M20 17a7 7 0 0 0 0 10M30 17a7 7 0 0 1 0 10" stroke="#fff" stroke-width="3" fill="none"/><circle cx="25" cy="22" r="3" fill="#fff"/><rect x="6" y="36" width="38" height="10" rx="2" fill="#fff"/></svg><div><h4>Lorem Ipsum is simply dummy text</h4><p>Lorem Ipsum is simply dummy text of the<br>printing and typesetting industry.</p></div></div>
      <div class="service"><svg width="50" height="46" viewBox="0 0 50 46"><rect x="17" y="2" width="16" height="12" fill="#fff"/><rect x="2" y="32" width="16" height="12" fill="#fff"/><rect x="32" y="32" width="16" height="12" fill="#fff"/><path d="M25 14v9M10 32v-9h30v9" stroke="#fff" stroke-width="3" fill="none"/></svg><div><h4>Lorem Ipsum is simply dummy text</h4><p>Lorem Ipsum is simply dummy text of the<br>printing and typesetting industry.</p></div></div>
      <div class="service"><svg width="50" height="50" viewBox="0 0 50 50"><circle cx="32" cy="18" r="11" stroke="#fff" stroke-width="6" stroke-dasharray="4 3" fill="none"/><circle cx="14" cy="36" r="8" stroke="#fff" stroke-width="5" stroke-dasharray="3 3" fill="none"/></svg><div><h4>Lorem Ipsum is simply dummy text</h4><p>Lorem Ipsum is simply dummy text of the<br>printing and typesetting industry.</p></div></div>
      <div class="service"><svg width="50" height="50" viewBox="0 0 50 50"><rect x="6" y="4" width="38" height="12" rx="2" fill="#fff"/><rect x="6" y="19" width="38" height="12" rx="2" fill="#fff"/><rect x="6" y="34" width="38" height="12" rx="2" fill="#fff"/></svg><div><h4>Lorem Ipsum is simply dummy text</h4><p>Lorem Ipsum is simply dummy text of the<br>printing and typesetting industry.</p></div></div>
    </div>
  </section>
  <div class="divider" style="top:338px"></div>

  <section class="stats">
    <h2><span>Zorpax Servers -</span> check out our stats!</h2>
    <div class="stat-row">
      <div class="stat"><span class="ic"></span><div><b>2,500,000</b><small>Domains registered in over<br>250 extensions</small></div></div>
      <div class="stat"><span class="ic"></span><div><b>50,000</b><small>new registrations<br>per month</small></div></div>
      <div class="stat"><span class="ic"></span><div><b>800,000</b><small>new registrations<br>per month</small></div></div>
      <div class="stat"><span class="ic"></span><div><b>1,000,000</b><small>clients are using our products</small></div></div>
    </div>
  </section>
  <div class="divider" style="top:548px"></div>

  <section class="footer-cols">
    <div class="col-about">
      <h3>Lorem Ipsum is simply dummy text</h3>
      <p>Lorem Ipsum is simply dummy text of the printing and<br>typesetting industry. Lorem Ipsum has been the<br>industry's standard dummy text ever since the 1500s,<br>when an unknown printer took a galley of type and<br>scrambled it to make a type specimen book.</p>
      <a href="#">Learn more about it.</a>
    </div>
    <div class="col-links">
      <h3>About Zorpax Servers</h3>
      <ul><li>About Us</li><li>Latest News</li><li>Domains</li><li>My Account</li><li>Web Hosting</li><li>Contact Us</li></ul>
      <p>Copyright © Zorpax Servers Ltd 2012.<br>All rights reserved</p>
    </div>
    <div class="col-info">
      <h3>Information</h3>
      <p>Contact us via our Support Ticket System in your Online Control Panel or alternatively call us on the number below:</p>
      <p class="phone">01632 960 418</p>
      <div class="social"><span style="background:#3b5a9a"></span><span style="background:#3aa4dd"></span><span style="background:#f07d1e"></span></div>
    </div>
  </section>

  <div class="bottom-strip">
    <div class="logos" aria-label="Partners">
      <span style="width:50px;height:50px;border-radius:50%"></span>
      <span style="width:92px;height:22px"></span>
      <span style="width:92px;height:26px"></span>
      <span style="width:88px;height:30px"></span>
      <span style="width:36px;height:36px"></span>
      <span style="width:110px;height:22px"></span>
      <span style="width:64px;height:40px;border-radius:50%"></span>
    </div>
    <div class="award"><div><b>AWARD WINNING</b><span style="font-size:13px">DEDICATED HOSTING</span><br><em>View Our Awards</em></div><div class="seal" role="img" aria-label="Award seal"></div></div>
    <span class="sitemap">SHOW SITEMAP</span>
  </div>
</footer>

</body>
</html>
```